Business card for STEADYWAVE

Please design professional business card for IT consulting firm STEADYWAVE INC.
Use logo attached.
Use information from sample qNode business card attached.
replace qnode inc with STEADYWAVE INC.
as well as qnodeinc.com with steadywave.example

```html
<!DOCTYPE html>
<html lang="en">
<head>
<meta charset="utf-8">
<title>STEADYWAVE business card</title>
<link rel="stylesheet" href="https://fonts.googleapis.com/css2?family=Jost:wght@400;500;600&display=swap">
<style>
  :root {
    --page: #dcdcdc;
    --card: #1e1e1e;
    --card-edge: #2a2a2a;
    --ink: #ffffff;
    --ink-soft: #e8e8e8;
    --rule: #9a9a9a;
    --logo-back: #8c8c8c;
    --accent: #3fc9b4;
  }
  * { margin: 0; padding: 0; box-sizing: border-box; }
  html, body { width: 1200px; height: 1200px; overflow: hidden; }
  body {
    background: var(--page);
    font-family: "Jost", "Futura", sans-serif;
    color: var(--ink);
    position: relative;
  }
  .card {
    position: absolute;
    left: 150px;
    width: 900px;
    height: 514px;
    background: linear-gradient(135deg, var(--card) 0%, var(--card-edge) 60%, #333 100%);
    overflow: hidden;
  }
  .card--front { top: 56px; }
  .card--back { top: 630px; }

  .wordmark {
    position: absolute;
    display: flex;
    align-items: center;
    gap: 16px;
    font-weight: 500;
    letter-spacing: 0.08em;
    line-height: 1;
    white-space: nowrap;
  }
  .wordmark__dot {
    width: 0.5em;
    height: 0.5em;
    background: currentColor;
  }
  .card--front .wordmark {
    right: 64px;
    top: 60px;
    font-size: 58px;
    color: var(--ink);
  }
  .card--back .wordmark {
    left: 50%;
    top: 50%;
    transform: translate(-50%, -50%);
    font-size: 76px;
    color: var(--logo-back);
  }

  .person {
    position: absolute;
    left: 62px;
    top: 250px;
  }
  .person__name {
    font-size: 27px;
    font-weight: 600;
    letter-spacing: 0.01em;
  }
  .person__role {
    font-size: 20px;
    font-weight: 400;
    letter-spacing: 0.08em;
    margin-top: -2px;
  }
  .divider {
    position: absolute;
    left: 61px;
    width: 775px;
    top: 314px;
    height: 1px;
    background: var(--rule);
  }
  .contacts {
    position: absolute;
    left: 62px;
    top: 326px;
    list-style: none;
    font-size: 21px;
    line-height: 27px;
    color: var(--ink-soft);
  }
  .contacts li { display: flex; align-items: center; gap: 12px; }
  .contacts svg { width: 20px; height: 20px; fill: var(--ink); flex: none; }
  .company {
    position: absolute;
    right: 70px;
    top: 326px;
    text-align: right;
    font-size: 21px;
    line-height: 27px;
    font-style: normal;
    color: var(--ink-soft);
  }
  .company__name { font-weight: 600; color: var(--ink); }
  .band {
    position: absolute;
    left: 0; right: 0; bottom: 0;
    height: 25px;
    background: var(--accent);
  }
</style>
</head>
<body>
  <section class="card card--front">
    <div class="wordmark">STEADYWAVE<span class="wordmark__dot"></span></div>

    <div class="person">
      <div class="person__name">DORIAN VELASKO, P.ENG.</div>
      <div class="person__role">GENERAL MANAGER</div>
    </div>

    <div class="divider"></div>

    <ul class="contacts">
      <li>
        <svg viewBox="0 0 24 24" aria-hidden="true"><path d="M6.6 10.8a15 15 0 0 0 6.6 6.6l2.2-2.2a1 1 0 0 1 1-.25 11.4 11.4 0 0 0 3.6.57 1 1 0 0 1 1 1V20a1 1 0 0 1-1 1A17 17 0 0 1 3 4a1 1 0 0 1 1-1h3.5a1 1 0 0 1 1 1c0 1.25.2 2.45.57 3.57a1 1 0 0 1-.25 1z"/></svg>
        (555) 014-2270 ext.201
      </li>
      <li>
        <svg viewBox="0 0 24 24" aria-hidden="true"><path d="M7 1h10a2 2 0 0 1 2 2v18a2 2 0 0 1-2 2H7a2 2 0 0 1-2-2V3a2 2 0 0 1 2-2zm0 3v14h10V4zm5 15.5a1 1 0 1 0 0 2 1 1 0 0 0 0-2z"/></svg>
        (555) 019-3384
      </li>
      <li>
        <svg viewBox="0 0 24 24" aria-hidden="true"><path d="M2 6h20v13H2zm2 2v.5l8 5 8-5V8l-8 5z"/></svg>
        dvelasko@steadywave.example
      </li>
      <li>
        <svg viewBox="0 0 24 24" aria-hidden="true"><path d="M12 2a10 10 0 1 0 0 20 10 10 0 0 0 0-20zm-1 17.9A8 8 0 0 1 4.2 10.2L9 15v1a2 2 0 0 0 2 2zm6.9-2.5A2 2 0 0 0 16 16h-1v-3a1 1 0 0 0-1-1H8v-2h2a1 1 0 0 0 1-1V7h2a2 2 0 0 0 2-2v-.4a8 8 0 0 1 2.9 12.8z"/></svg>
        www.steadywave.example
      </li>
    </ul>

    <address class="company">
      <div class="company__name">STEADYWAVE INC</div>
      <div>2180 Harbourline Rd.,</div>
      <div>Suite 101, Fairhaven</div>
      <div>Ontario, L4K 2M8, Canada</div>
    </address>

    <div class="band"></div>
  </section>

  <section class="card card--back">
    <div class="wordmark">STEADYWAVE<span class="wordmark__dot"></span></div>
  </section>
</body>
</html>
```